Cigar Ring Design

we are working on a project, which is an eCommerce store for cigars, now instead of selling all kind of existing brands this project is based on a BrassMeadowHouse concept where an outlet is linked to an actual Cigar factory,
so the cigar lines sold will come out under a BMH (BrassMeadowHouse) brand consisting of various labels, (think Barney Kettle, Harbor Crest, Willow Crest etc) I had an idea for the Cigar Rings for this project, where I put BM in an O (circle) of which I made mock ups (see attachement), now I am not a designer, I am sure a real designer can come up with something more stylish and unique.

```html
<!DOCTYPE html>
<html lang="en">
<head>
<meta charset="UTF-8">
<title>Moss Crest Cigar Ring – BMH</title>
<link rel="stylesheet" href="https://fonts.googleapis.com/css2?family=Fira+Sans+Condensed:wght@800&family=Montserrat:wght@800&display=swap">
<style>
  :root {
    --page: #ffffff;
    --band-deep: #033d0f;
    --band-mid: #0a5a17;
    --band-glow: #137a1f;
    --gold-light: #f6d27a;
    --gold: #d9a53a;
    --gold-dark: #8a5a12;
    --ink-green: #003c0c;
    --white: #ffffff;
  }
  * { margin: 0; padding: 0; box-sizing: border-box; }
  html, body {
    width: 1200px; height: 600px; overflow: hidden;
    background: var(--page);
  }
  .canvas { position: relative; width: 1200px; height: 600px; }

  .ring-band {
    position: absolute; left: 101px; top: 143px;
    width: 914px; height: 314px;
    border-radius: 0 60px 60px 0;
    overflow: hidden;
    background:
      radial-gradient(ellipse 300px 220px at 420px 130px, var(--band-glow) 0%, var(--band-mid) 45%, transparent 100%),
      linear-gradient(180deg, var(--band-mid), var(--band-deep));
  }
  .ornament-arc { position: absolute; left: 0; top: 0; }

  .label-title {
    position: absolute; left: 187px; top: 268px;
    font-family: "Fira Sans Condensed", sans-serif;
    font-weight: 800; font-size: 44px; line-height: 1;
    color: var(--white); letter-spacing: 0.5px;
  }
  .label-rule { position: absolute; left: 189px; top: 332px; }
  .label-sub {
    position: absolute; left: 294px; top: 333px; width: 64px;
    text-align: center;
    font-family: "Montserrat", sans-serif; font-weight: 800;
    font-size: 17px; letter-spacing: 5px; line-height: 1;
    color: var(--white);
  }

  .coin { position: absolute; }
  .coin--large { left: 535px; top: 194px; }
  .coin--small { left: 952px; top: 252px; }
  .coin-mark {
    font-family: "Fira Sans Condensed", sans-serif;
    font-weight: 800; fill: var(--ink-green);
  }
</style>
</head>
<body>
<main class="canvas">
  <section class="ring-band">
    <svg class="ornament-arc" width="914" height="314" viewBox="0 0 914 314" role="img" aria-label="Gold Greek key ornament sweeping along the left of the band">
      <defs>
        <linearGradient id="arcGold" x1="0" y1="0" x2="1" y2="1">
          <stop offset="0" stop-color="#c8901c" stop-opacity="0.75"/>
          <stop offset="0.6" stop-color="#a86b12" stop-opacity="0.6"/>
          <stop offset="1" stop-color="#5a2a08" stop-opacity="0.7"/>
        </linearGradient>
      </defs>
      <path d="M0 0 L320 0 A420 420 0 0 0 150 314 L0 314 Z" fill="url(#arcGold)" opacity="0.55"/>
      <path d="M320 0 A420 420 0 0 0 150 314 L128 314 A440 440 0 0 1 300 0 Z" fill="#c8901c" opacity="0.5"/>
    </svg>
  </section>

  <h1 class="label-title">MOSS CREST</h1>
  <svg class="label-rule" width="274" height="16" viewBox="0 0 274 16" aria-hidden="true">
    <polygon points="0,3 105,2 0,15" fill="var(--white)"/>
    <polygon points="168,2 273,3 273,15" fill="var(--white)"/>
  </svg>
  <p class="label-sub">BMH</p>

  <svg class="coin coin--large" width="212" height="212" viewBox="0 0 212 212">
    <defs>
      <radialGradient id="goldFace" cx="0.4" cy="0.35" r="0.75">
        <stop offset="0" stop-color="var(--gold-light)"/>
        <stop offset="0.7" stop-color="var(--gold)"/>
        <stop offset="1" stop-color="var(--gold-dark)"/>
      </radialGradient>
    </defs>
    <circle cx="106" cy="106" r="105" fill="url(#goldFace)" role="img" aria-label="Gold Greek key border ring of the coin"/>
    <circle cx="106" cy="106" r="71" fill="var(--gold-light)"/>
    <text class="coin-mark" x="106" y="128" text-anchor="middle" font-size="62">BM</text>
  </svg>

  <svg class="coin coin--small" width="96" height="96" viewBox="0 0 96 96">
    <circle cx="48" cy="48" r="47" fill="url(#goldFace)"/>
    <circle cx="48" cy="48" r="41" fill="var(--gold-light)"/>
    <text class="coin-mark" x="48" y="60" text-anchor="middle" font-size="34">BM</text>
  </svg>
</main>
</body>
</html>
```